Business card design needed

Our company background is that we provides transfers to and from the airport, social & corporate events, weddings.
We are also available for charter for birthday party, wine tastings, concerts, anniversary, school balls etc.
Our business cards have to reflect that we have a professional company, they are our first contact and have to stand out from the other 'players' in the market.

Industry/Entity Type

School

Contact Information for Business Card

VESTAR PTH, Teodor & Marguerite, mob: 0427 381 592, PO Box 284, Calderwood WA 6972, ABN 52 614 203 178, Lic 7169/2058,

Requirements
Must have
• Telephone number: 0427 381 592
Website: www.VESTARPTH.com.au
postal address: PO Box 284, Calderwood WA 6972
Licences: Lic 7169/2058

***If using the new photo (one with the bus and buildings behind it), if possible can the buildings be cropped out. Thanks
Nice to have
• would be nice to have the pics of the vehicle(s), preferred the Vel on the card but not too fussed.
Should not have
• Picture of vehicle we don't have in our fleet. (We ONLY have the Velarions and Murako Densa mini bus)

```html
<!DOCTYPE html>
<html lang="en">
<head>
<meta charset="utf-8">
<title>Vestar Chauffeur &amp; Charter Services – Business Card</title>
<link rel="stylesheet" href="https://fonts.googleapis.com/css2?family=Open+Sans:wght@400&display=swap">
<style>
  :root {
    --ink: #0a0a0a;
    --panel-top: #1c1c1c;
    --panel-bottom: #4a4a4a;
    --text: #f2f2f2;
    --rule: #e8e8e8;
    --silver-light: #d9d4c6;
    --silver-mid: #a39d8e;
    --silver-dark: #3a3833;
  }
  html, body {
    margin: 0;
    padding: 0;
    width: 1200px;
    height: 741px;
    overflow: hidden;
    background: var(--ink);
  }
  .card {
    position: relative;
    width: 1200px;
    height: 741px;
    background: var(--ink);
    font-family: "Open Sans", Arial, sans-serif;
    color: var(--text);
    overflow: hidden;
  }
  .contact-panel {
    position: absolute;
    left: 0;
    top: 0;
    width: 430px;
    height: 741px;
    background: linear-gradient(30deg, var(--panel-bottom) 0%, #2f2f2f 45%, var(--panel-top) 100%);
  }
  .owners {
    position: absolute;
    left: 48px;
    top: 274px;
    margin: 0;
    font-size: 29px;
    font-weight: 400;
    letter-spacing: 1px;
    white-space: nowrap;
  }
  .owners-rule {
    position: absolute;
    left: 48px;
    top: 340px;
    width: 305px;
    height: 2px;
    background: var(--rule);
  }
  .details {
    position: absolute;
    left: 48px;
    top: 0;
    margin: 0;
    padding: 0;
    list-style: none;
    font-size: 19.5px;
    font-weight: 400;
    letter-spacing: 0.3px;
  }
  .details li {
    position: absolute;
    left: 0;
    white-space: nowrap;
  }
  .details .mobile { top: 385px; }
  .details .postal { top: 434px; }
  .details .abn { top: 492px; }
  .details .licence { top: 540px; }
  .details .web { top: 589px; }

  .brand {
    position: absolute;
    right: 87px;
    top: 86px;
    text-align: right;
  }
  .brand-name {
    margin: 0;
    font-size: 80px;
    font-weight: 400;
    line-height: 1;
    letter-spacing: 3px;
  }
  .brand-tagline {
    margin: 14px 0 0;
    font-size: 19px;
    font-weight: 400;
    letter-spacing: 0.5px;
  }
  .vehicle-photo {
    position: absolute;
    left: 492px;
    top: 337px;
    width: 648px;
    height: 312px;
    border-radius: 90px 120px 40px 40px / 70px 90px 30px 30px;
    background: radial-gradient(ellipse at 40% 40%, var(--silver-light) 0%, var(--silver-mid) 50%, var(--silver-dark) 100%);
  }
</style>
</head>
<body>
  <main class="card">
    <section class="contact-panel">
      <h1 class="owners">TEODOR &amp; MARGUERITE</h1>
      <div class="owners-rule"></div>
      <ul class="details">
        <li class="mobile">Mobile : 0427 381 592</li>
        <li class="postal">PO Box 284, Calderwood WA 6972</li>
        <li class="abn">ABN 52 614 203 178</li>
        <li class="licence">Lic 7169/2058</li>
        <li class="web">www.vestarpth.com.au</li>
      </ul>
    </section>

    <header class="brand">
      <p class="brand-name">VESTAR</p>
      <p class="brand-tagline">CHAUFFEUR &amp; CHARTER SERVICES</p>
    </header>

    <div class="vehicle-photo" role="img" aria-label="Photo of a silver Velarion luxury sedan, front three-quarter view"></div>
  </main>
</body>
</html>
```